Business Card Design for company

We want new business cards. We'd like something different-- yet still highly professional. Our tagline is Providing leadership, delivering success. Stock photos are ok, as long as they are relevant and look upscale.

Target Market(s)

Architecture/Business Management Consulting/Engineering Consulting

Contact Information for Business Card

dark gray background with pops of blue might be good, but you tell me. You're the designers. Rounded corners might be nice, but again, you tell me.

Font styles to use
Serif
Sans Serif

Colors
3276b5
5c5c5c
9d9d9d
fbfbfb

Requirements
Nice to have
• Something different, but still very professional.

```html
<!DOCTYPE html>
<html lang="en">
<head>
<meta charset="utf-8">
<title>Norvale International – Business Card</title>
<link rel="stylesheet" href="https://fonts.googleapis.com/css2?family=Montserrat:wght@600;700&family=Nunito+Sans:ital,wght@0,400;1,400&display=swap">
<style>
  :root {
    --card-grey: #5c5c5c;
    --accent-blue: #3276b5;
    --soft-grey: #9d9d9d;
    --paper-white: #fbfbfb;
    --backdrop: #e4e5e7;
  }
  html, body {
    margin: 0;
    padding: 0;
    width: 1154px;
    height: 1200px;
    overflow: hidden;
    background: var(--backdrop);
  }
  .sheet {
    position: relative;
    width: 1154px;
    height: 1200px;
  }
  .card {
    position: absolute;
    left: 127px;
    width: 900px;
    height: 515px;
    background: var(--card-grey);
    border-radius: 30px;
    overflow: hidden;
    box-shadow: 0 6px 18px rgba(0,0,0,0.18);
    color: var(--paper-white);
  }
  .card--front { top: 55px; }
  .card--back  { top: 630px; }

  .accent-bar {
    position: absolute;
    height: 72px;
    background: var(--accent-blue);
  }
  .card--front .accent-bar--top    { left: 275px; top: 0;   width: 350px; }
  .card--front .accent-bar--bottom { left: 335px; bottom: 0; width: 350px; }
  .card--back  .accent-bar--top    { left: 70px;  top: 0;   width: 320px; }
  .card--back  .accent-bar--bottom { left: 40px;  bottom: 0; width: 320px; }

  .brand-name {
    font-family: "Montserrat", sans-serif;
    font-weight: 700;
    color: var(--paper-white);
    margin: 0;
    text-align: center;
    line-height: 1.05;
  }
  .card--front .brand-name {
    position: absolute;
    left: 0; right: 0;
    top: 140px;
    font-size: 64px;
    letter-spacing: 2px;
  }
  .brand-name__sub {
    display: block;
    font-size: 0.55em;
    letter-spacing: 3px;
    margin-top: 10px;
  }
  .tagline {
    position: absolute;
    left: 0; right: 0;
    top: 338px;
    margin: 0;
    text-align: center;
    font-family: "Montserrat", sans-serif;
    font-weight: 600;
    font-size: 21px;
    letter-spacing: 1.5px;
    line-height: 1.2;
  }

  .card--back .brand-name {
    position: absolute;
    left: 60px;
    width: 360px;
    top: 185px;
    font-size: 52px;
    letter-spacing: 1px;
  }
  .divider {
    position: absolute;
    left: 455px;
    top: 135px;
    width: 2px;
    height: 235px;
    background: var(--paper-white);
  }
  .contact {
    position: absolute;
    left: 500px;
    top: 140px;
    font-family: "Nunito Sans", sans-serif;
    font-size: 20px;
    line-height: 1.3;
  }
  .contact__name {
    margin: 0;
    font-family: "Montserrat", sans-serif;
    font-weight: 700;
    font-size: 29px;
    letter-spacing: 1.5px;
  }
  .contact__role {
    margin: 0 0 18px;
    font-style: italic;
    font-size: 25px;
  }
  .contact__block {
    margin: 0 0 14px;
    font-style: normal;
  }
</style>
</head>
<body>
<main class="sheet">
  <section class="card card--front" aria-label="Card front">
    <div class="accent-bar accent-bar--top"></div>
    <h1 class="brand-name">NORVALE<span class="brand-name__sub">INTERNATIONAL</span></h1>
    <p class="tagline">GUIDING STRATEGY<br>BUILDING LASTING RESULTS</p>
    <div class="accent-bar accent-bar--bottom"></div>
  </section>

  <section class="card card--back" aria-label="Card back">
    <div class="accent-bar accent-bar--top"></div>
    <h2 class="brand-name">NORVALE<span class="brand-name__sub">INTERNATIONAL</span></h2>
    <div class="divider"></div>
    <div class="contact">
      <p class="contact__name">DANIEL R. WHITFIELD</p>
      <p class="contact__role">President</p>
      <address class="contact__block">4180 Harbor Crest Lane<br>Tampa, FL 33602</address>
      <p class="contact__block">(888) 555-0142<br>info@norvaleintl.com</p>
      <p class="contact__block">www.norvaleintl.com</p>
    </div>
    <div class="accent-bar accent-bar--bottom"></div>
  </section>
</main>
</body>
</html>
```